Box for baby swaddle blankets.

Hi there!

I'd like you to make a packaging design for the box of my muslin swaddle blankets which I'll be selling on Pindlewick.com. I want the product to be the perfect baby shower gift! Most of the packages of my competitors are made by the manufacturing company, so they're pretty simple and similar to each other, I'd like you to make a unique design for me. I included a detailed description about the parameters in the "must haves" section. If you have any questions or suggestions, please message me.

Target Market(s)

Pindlewick.com

Industry/Entity Type

Baby Care

Colors

Designer to choose colors to be used in the design.

Requirements
Must have
• 1. Most of my competitors use pretty basic packaging, so I'd like stand out with my box. I was thinking about putting my logo at the bottom of the front side, and make heart-shaped cuts above the elephant's trunk, which would allow buyers to see the fabric and the pattern of the blankets. You can remove the heart from my logo since I think it wouldn't look good with the cuts above it. Tell me what you think about this, I'm also open for other ideas for the front as well as long as it makes the packaging unique and gives the buyers a peek of the blankets.
• I attached some examples of cuts I've seen on packages.
• 2. I'd like you to use the title BABY SWADDLE BLANKETS and my logo on the front. The package contains 3 blankets are made from organic muslin cotton with 47x47 inch size, you could include this also in the front if you can find a good way for it .
• Also, I'd like to have a stamp of 100% ORGANIC COTTON in one corner.
• The package will contain a bonus baby bandana bib, so please put a BANDANA BIB GIFT INSIDE! object with an arrow pointing in the box in the front.
• 3. For the sides, one of them should show the different ways you can use these blankets, with illustrations. I'll attach some examples for this (I like the pictogram-type illustration on img1 better) . You can add my logo for the top side. You can try to add the words "BREATHABLE" "EXTRA SOFT" "LARGE SIZE" "100% ORGANIC COTTON" on the remaining side(s) if it would look good in your opinion.
• 4. For the back, I'd like you to add a 4-step instruction about how to swaddle the baby with the blankets. Since almost all of competitors use the same images, I'd like you to design new ones, make it playful and baby-friendly :) I'll attach some examples for these instructions as well.. The bottom of the back should contain the text "Made with care in China, designed with love in the United States" and a place for the barcode.
• 4. The box should be the size of 21*22*8 in centimeters.
• If you have any questions or suggestions for the design, please message me.
Nice to have
• If you have any other ideas or suggestions about the design, feel free to contact me.

```html
<!DOCTYPE html>
<html lang="en">
<head>
<meta charset="utf-8">
<title>Snugglory Baby Swaddle Blankets – Box Front and Side</title>
<link rel="stylesheet" href="https://fonts.googleapis.com/css2?family=Amatic+SC:wght@400;700&family=Josefin+Sans:wght@300;400;700&display=swap">
<style>
  :root {
    --sand: #eedfcb;
    --mist: #eef5f7;
    --sky: #3ba3d9;
    --sky-soft: #8cc9ea;
    --teal: #1aa597;
    --lemon: #f2efbe;
    --ink: #1d1d1b;
    --page: #ffffff;
  }
  html, body {
    margin: 0;
    padding: 0;
    width: 1200px;
    height: 1015px;
    overflow: hidden;
    background: var(--page);
  }
  p, h1 { margin: 0; }
  .canvas {
    position: relative;
    width: 1200px;
    height: 1015px;
  }

  /* Front panel */
  .front-panel {
    position: absolute;
    left: 98px;
    top: 128px;
    width: 747px;
    height: 700px;
    background: var(--sand);
  }
  .tagline {
    position: absolute;
    left: 0;
    width: 720px;
    top: 56px;
    text-align: center;
    font-family: "Josefin Sans", sans-serif;
    font-weight: 300;
    font-size: 21px;
    line-height: 1;
    letter-spacing: 0.5px;
    color: var(--sky);
  }
  .title {
    position: absolute;
    left: 0;
    width: 748px;
    top: 100px;
    text-align: center;
    font-family: "Amatic SC", sans-serif;
    font-weight: 700;
    font-size: 62px;
    letter-spacing: 8px;
    line-height: 1;
    color: var(--ink);
  }
  .material-ribbon {
    position: absolute;
    left: 200px;
    top: 180px;
    width: 340px;
    height: 70px;
  }
  .material-ribbon text {
    font-family: "Josefin Sans", sans-serif;
    font-weight: 400;
    font-size: 12px;
    letter-spacing: 1px;
    fill: var(--ink);
  }
  .gift-badge {
    position: absolute;
    left: 600px;
    top: -8px;
    width: 130px;
    height: 140px;
  }
  .gift-badge text {
    font-family: "Josefin Sans", sans-serif;
    font-weight: 700;
    fill: var(--ink);
    text-anchor: middle;
  }
  .window-row {
    position: absolute;
    left: 40px;
    top: 282px;
    width: 690px;
    height: 175px;
  }
  .scatter-hearts {
    position: absolute;
    left: 245px;
    top: 390px;
    width: 200px;
    height: 120px;
  }
  .brand-lockup {
    position: absolute;
    left: 250px;
    top: 595px;
    width: 260px;
    text-align: center;
    font-family: "Josefin Sans", sans-serif;
    font-weight: 400;
    font-size: 46px;
    line-height: 1;
    color: var(--sky);
  }
  .count {
    position: absolute;
    left: 31px;
    top: 615px;
    font-family: "Amatic SC", sans-serif;
    font-weight: 700;
    font-size: 40px;
    line-height: 1;
    letter-spacing: 2px;
    color: var(--ink);
  }
  .size-tag {
    position: absolute;
    left: 567px;
    top: 612px;
    width: 126px;
    height: 43px;
    border-radius: 3px;
    background: var(--mist);
    text-align: center;
    line-height: 43px;
    font-family: "Amatic SC", sans-serif;
    font-weight: 700;
    font-size: 28px;
    letter-spacing: 1px;
    color: var(--ink);
  }

  /* Side panel */
  .side-panel {
    position: absolute;
    left: 918px;
    top: 125px;
    width: 176px;
    height: 700px;
  }
  .side-label {
    position: absolute;
    left: 24px;
    top: 43px;
    width: 130px;
    height: 449px;
    border-radius: 16px;
    background: var(--sand);
  }
  .side-brand {
    position: absolute;
    left: 0;
    top: 80px;
    width: 130px;
    text-align: center;
    font-family: "Josefin Sans", sans-serif;
    font-weight: 400;
    font-size: 22px;
    line-height: 1;
    color: var(--sky);
  }
</style>
</head>
<body>
<main class="canvas">

  <section class="front-panel" aria-label="Box front">
    <p class="tagline">EXTRA SOFT</p>
    <h1 class="title">BABY SWADDLE BLANKETS</h1>

    <svg class="material-ribbon" viewBox="0 0 340 70" aria-label="100% organic muslim cotton">
      <path d="M0 58 L20 38 L12 24 Q170 -2 328 24 L320 38 L340 58 Q170 28 0 58 Z" fill="var(--mist)"/>
      <path id="ribbon-arc" d="M40 40 Q170 16 300 40" fill="none"/>
      <text><textPath href="#ribbon-arc" startOffset="50%" text-anchor="middle">100% ORGANIC MUSLIM COTTON</textPath></text>
    </svg>

    <svg class="gift-badge" viewBox="0 0 130 140" aria-label="Bandana bib gift inside">
      <path d="M40 90 L62 124 L70 108 Z" fill="var(--lemon)"/>
      <path d="M70 100 L100 126 L100 104 Z" fill="var(--lemon)"/>
      <circle cx="62" cy="60" r="55" fill="var(--lemon)" stroke="var(--teal)" stroke-width="5"/>
      <text x="62" y="42" font-size="12">BANDANA</text>
      <text x="64" y="58" font-size="12">BIB</text>
      <text x="66" y="77" font-size="16">GIFT</text>
      <text x="66" y="92" font-size="11">INSIDE!</text>
    </svg>

    <svg class="window-row" viewBox="0 0 690 175">
      <defs>
        <linearGradient id="fabric-trees" x1="0" y1="0" x2="1" y2="1">
          <stop offset="0" stop-color="#dcedf3"/>
          <stop offset="1" stop-color="#b9e0da"/>
        </linearGradient>
        <linearGradient id="fabric-waves" x1="0" y1="0" x2="0" y2="1">
          <stop offset="0" stop-color="#dcecf4"/>
          <stop offset="1" stop-color="#c6e3f0"/>
        </linearGradient>
        <linearGradient id="fabric-whales" x1="0" y1="0" x2="1" y2="1">
          <stop offset="0" stop-color="#cfeee9"/>
          <stop offset="1" stop-color="#e6e1d8"/>
        </linearGradient>
        <path id="heart-window" d="M95 172 C60 140 0 105 0 50 C0 18 24 0 50 0 C72 0 88 12 95 28 C102 12 118 0 140 0 C166 0 190 18 190 50 C190 105 130 140 95 172 Z"/>
      </defs>
      <use href="#heart-window" x="0" fill="url(#fabric-trees)" role="img" aria-label="Blanket fabric seen through a heart cut, mountain and tree print"/>
      <use href="#heart-window" x="242" fill="url(#fabric-waves)" role="img" aria-label="Blanket fabric seen through a heart cut, sun and wave print"/>
      <use href="#heart-window" x="490" fill="url(#fabric-whales)" role="img" aria-label="Blanket fabric seen through a heart cut, whale print"/>
    </svg>

    <svg class="scatter-hearts" viewBox="0 0 200 120" aria-hidden="true">
      <defs>
        <path id="mini-heart" d="M0 4 C0 -2 8 -2 8 4 C8 -2 16 -2 16 4 C16 10 8 14 8 18 C8 14 0 10 0 4 Z"/>
      </defs>
      <g fill="var(--sky-soft)">
        <use href="#mini-heart" transform="translate(10 26) rotate(-20) scale(1.2)"/>
        <use href="#mini-heart" transform="translate(60 0) scale(1)"/>
        <use href="#mini-heart" transform="translate(40 52) rotate(15) scale(0.9)"/>
        <use href="#mini-heart" transform="translate(70 72) rotate(-10) scale(0.8)"/>
        <use href="#mini-heart" transform="translate(105 80) rotate(20) scale(0.8)"/>
        <use href="#mini-heart" transform="translate(2 100) rotate(-35) scale(1.1)"/>
        <use href="#mini-heart" transform="translate(160 42) rotate(-25) scale(1)"/>
      </g>
    </svg>

    <div class="brand-lockup">Snugglory</div>
    <p class="count">3 BLANKETS</p>
    <div class="size-tag">47X47</div>
  </section>

  <section class="side-panel" aria-label="Box side">
    <svg width="176" height="700" viewBox="0 0 176 700" aria-hidden="true">
      <rect x="0" y="0" width="176" height="700" fill="var(--mist)"/>
      <rect x="0" y="0" width="16" height="700" fill="var(--sand)"/>
      <rect x="48" y="0" width="32" height="700" fill="var(--sand)"/>
      <rect x="112" y="0" width="32" height="700" fill="var(--sand)"/>
      <g stroke="var(--ink)" stroke-width="1.5">
        <line x1="1" y1="0" x2="1" y2="700"/>
        <line x1="64" y1="0" x2="64" y2="700"/>
        <line x1="77" y1="0" x2="77" y2="700"/>
        <line x1="113" y1="0" x2="113" y2="700"/>
        <line x1="127" y1="0" x2="127" y2="700"/>
      </g>
      <g fill="var(--sky-soft)">
        <path d="M56 562 C56 554 66 554 66 562 C66 554 76 554 76 562 C76 570 66 574 66 580 C66 574 56 570 56 562 Z" transform="rotate(-15 66 566)"/>
        <path d="M94 592 C94 586 101 586 101 592 C101 586 108 586 108 592 C108 598 101 601 101 605 C101 601 94 598 94 592 Z"/>
        <path d="M110 600 C110 595 116 595 116 600 C116 595 122 595 122 600 C122 605 116 608 116 611 C116 608 110 605 110 600 Z" transform="rotate(20 116 603)"/>
        <path d="M46 632 C46 625 54 625 54 632 C54 625 62 625 62 632 C62 639 54 642 54 647 C54 642 46 639 46 632 Z" transform="rotate(-40 54 636)"/>
      </g>
    </svg>
    <div class="side-label">
      <div class="side-brand">Snugglory</div>
    </div>
  </section>

</main>
</body>
</html>
```